Bargo Finch

I want a design for a website where users can insert products URLs from different sites and the user will get notified by email when that product's price changes.

On the homepage I'd like a big input where the user can insert a product's URL. On the same page the following will appear:
- my products that I follow (options: share, buy, unfollow) + it's current price and deviation from last time it's price has changed (I may have many products that I follow, so maybe a table layout would be wise. - just a suggestion)
- products that other people follow (options: follow). If my Chatterloop friends follow a certain product, I can see their photo(eg: friend1, friend2 and 5 others are following this product) (also, may people may follow a product.)

On the login page I can register using user / pass or using Chatterloop

The 3rd page is the product's page. Once I click on any product I go to this page. On this page I can see:
- picture, name and price and no of people following this product
- a chart with the product's price over the last 30 days
- list with friends that follow this product (when logged in)
- product options: follow / unfollow, share, buy

Then I want the design for an email template that I send when 1 or more prices of a user's products change.

Nice to have: want level for product - describes how much wanted is a product after a certain internal algorithm

NB:
- flat design (not really kestra, something more like the new Vyra interface - just a suggestion)
- I'd prefer a red theme (based on the idea that the site will be represented by a rooster)
- don't forget the design for basic elements: loading screen, popup, alert, messages, etc

I've posted an initial prototype with what I'd like the design to contain.

• - flat design
- must be simple. much white space
• as few gradients as possible

```html
<!DOCTYPE html>
<html lang="en">
<head>
<meta charset="utf-8">
<title>Bargo Finch — Track product prices</title>
<link href="https://fonts.googleapis.com/css2?family=Mulish:wght@400;600;800&display=swap" rel="stylesheet">
<style>
:root{
  --red:#c50000;
  --red-btn:#d40a0a;
  --dark:#1c1c1c;
  --dark-2:#2b2b2b;
  --text:#333;
  --muted:#555;
  --line:#e2e2e2;
  --page:#f5f5f5;
  --white:#fff;
}
*{box-sizing:border-box;margin:0;padding:0}
html,body{width:829px;height:1200px;overflow:hidden}
body{position:relative;background:var(--page);font-family:"Mulish",Arial,sans-serif;color:var(--text)}
.abs{position:absolute}
.header-band{left:0;top:0;width:829px;height:148px;background:var(--red)}
.brand{left:88px;top:44px;display:flex;align-items:center;gap:8px;color:var(--white);font-weight:800;font-size:19px}
.brand-dot{width:14px;height:14px;border-radius:50%;background:var(--white)}
.top-search{left:566px;top:56px;width:138px;height:17px;background:var(--white);border-radius:2px;font-size:8px;color:#999;padding:4px 8px}
.go-btn{left:710px;top:56px;width:30px;height:17px;background:var(--dark);color:var(--white);font-size:9px;font-weight:600;text-align:center;line-height:17px;border-radius:2px}
.nav{left:88px;top:81px;width:652px;height:32px;background:linear-gradient(#2e2e2e,#121212);border:1px solid #000;border-radius:2px}
.nav-item{position:absolute;top:10px;font-size:10.5px;color:#eee}
.nav-search{position:absolute;left:487px;top:6px;width:160px;height:21px;background:var(--white);font-size:8.5px;color:#aaa;padding:5px 7px;border-radius:1px}
.hero{left:90px;top:123px;width:649px;height:276px;background:linear-gradient(100deg,#c9d8db 0%,#e3eced 45%,#d3e0e2 100%)}
.url-panel{left:117px;top:302px;width:595px;height:69px;background:var(--dark);border:1px solid #000;border-radius:2px}
.url-label{position:absolute;left:15px;top:10px;font-size:10px;color:#ddd}
.url-input{position:absolute;left:14px;top:29px;width:566px;height:31px;background:var(--dark-2);font-size:10px;color:#999;padding:10px 8px}
.url-submit{position:absolute;left:489px;top:32px;width:89px;height:25px;background:var(--red-btn);border:1px solid #900;border-radius:2px;color:var(--white);font-size:10.5px;font-weight:600;text-align:center;line-height:23px}
.dots{left:396px;top:380px;display:flex;gap:4px}
.dots i{width:10px;height:10px;border-radius:50%;background:var(--white)}
.dots i:first-child{background:var(--red)}
.section-title{left:89px;font-size:13.5px;color:#222}
.section-rule{left:89px;width:650px;height:1px;background:var(--line)}
.pager{left:698px;display:flex;gap:4px}
.pager span{width:18px;height:18px;border-radius:50%;background:#666;display:flex;align-items:center;justify-content:center}
.row{left:90px;width:649px;display:flex;justify-content:space-between}
.col{width:152px}
.card{height:106px;background:var(--white);border:1px solid #ddd;display:flex;align-items:center;justify-content:center}
.thumb{width:100px;height:70px;border-radius:3px}
.actions{display:flex;justify-content:space-between;margin-top:8px}
.act{width:49px;height:41px;background:linear-gradient(#fff,#ececec);border:1px solid #ccc;display:flex;flex-direction:column;align-items:center;justify-content:center;gap:4px;font-size:8.5px;color:#333}
.follow-btn{margin-top:8px;height:27px;background:linear-gradient(#fff,#e6e6e6);border:1px solid #bbb;border-radius:1px;display:flex;align-items:center;justify-content:center;gap:6px;font-size:12px;color:#333}
.friend-col{top:863px;width:152px;border-right:1px solid #e8e8e8}
.friend{display:flex;gap:6px;height:65px;margin-bottom:24px}
.avatar{width:70px;height:65px;border:1px solid #ccc;background:var(--white);padding:4px}
.avatar div{width:100%;height:100%}
.friend-name{font-size:10px;color:#444;margin-top:11px}
.following{margin-top:6px;width:62px;height:21px;background:linear-gradient(#fff,#eaeaea);border:1px solid #bbb;font-size:8.5px;color:#444;text-align:center;line-height:19px}
.friend-note{top:1035px;width:152px;font-size:8.7px;line-height:16px;color:#333;border-top:1px solid #eee;padding-top:4px}
.footer{left:0;top:1110px;width:829px;height:90px;background:var(--red)}
.foot-links{position:absolute;left:0;width:829px;top:22px;text-align:center;font-size:10px;color:var(--white);padding-right:20px}
.foot-copy{top:48px}
.foot-links span{margin:0 7px}
.social{position:absolute;left:647px;top:24px;display:flex;gap:4px}
.social i{width:22px;height:22px;border-radius:50%;background:#fff;opacity:.85}
</style>
</head>
<body>
<div class="abs header-band"></div>
<div class="abs brand"><span class="brand-dot"></span>Bargo Finch</div>
<div class="abs top-search">Search...</div>
<div class="abs go-btn">Go</div>
<nav class="abs nav">
  <span class="nav-item" style="left:19px">Home</span>
  <span class="nav-item" style="left:68px">About Us</span>
  <span class="nav-item" style="left:133px">Products URl</span>
  <span class="nav-item" style="left:216px">Testimonials</span>
  <span class="nav-item" style="left:295px">FAQ's</span>
  <span class="nav-item" style="left:343px">Contact Us</span>
  <div class="nav-search">Search</div>
</nav>

<div class="abs hero" role="img" aria-label="Man on the phone at a laptop in a bright office"></div>
<div class="abs url-panel">
  <div class="url-label">Insert Your Product URL</div>
  <div class="url-input">Enter Your Product URL</div>
  <div class="url-submit">Submit</div>
</div>
<div class="abs dots"><i></i><i></i><i></i><i></i></div>

<h2 class="abs section-title" style="top:420px;font-weight:400">My Products That I Follow</h2>
<div class="abs pager" style="top:418px">
  <span><svg width="8" height="8" viewBox="0 0 8 8"><path d="M5 1 2 4l3 3" stroke="#fff" stroke-width="1.6" fill="none"/></svg></span>
  <span><svg width="8" height="8" viewBox="0 0 8 8"><path d="M3 1l3 3-3 3" stroke="#fff" stroke-width="1.6" fill="none"/></svg></span>
</div>
<div class="abs section-rule" style="top:446px"></div>

<div class="abs row" style="top:472px">
  <div class="col"><div class="card"><div class="thumb" role="img" aria-label="Set of dark grooming bottles" style="background:linear-gradient(#3c4a55,#1b2228)"></div></div>
    <div class="actions">
      <div class="act"><svg width="17" height="12" viewBox="0 0 17 12"><path d="M0 1h6l2 2h9v9H0z" fill="#111"/></svg>Share</div>
      <div class="act"><svg width="16" height="13" viewBox="0 0 16 13"><path d="M0 1h3l2 8h9l2-6H4" stroke="#111" stroke-width="1.4" fill="none"/><circle cx="6" cy="11.5" r="1.3"/><circle cx="13" cy="11.5" r="1.3"/></svg>Buy</div>
      <div class="act"><svg width="14" height="13" viewBox="0 0 14 13"><path d="M5 0 0 4l5 4V5.5c4 0 7 1.5 8 6.5 0-6-3-9-8-9z" fill="#111"/></svg>Unfollow</div>
    </div></div>
  <div class="col"><div class="card"><div class="thumb" role="img" aria-label="Set of green and amber body care bottles" style="background:linear-gradient(#b99a6a,#6b7d3a)"></div></div>
    <div class="actions">
      <div class="act"><svg width="17" height="12" viewBox="0 0 17 12"><path d="M0 1h6l2 2h9v9H0z" fill="#111"/></svg>Share</div>
      <div class="act"><svg width="16" height="13" viewBox="0 0 16 13"><path d="M0 1h3l2 8h9l2-6H4" stroke="#111" stroke-width="1.4" fill="none"/><circle cx="6" cy="11.5" r="1.3"/><circle cx="13" cy="11.5" r="1.3"/></svg>Buy</div>
      <div class="act"><svg width="14" height="13" viewBox="0 0 14 13"><path d="M5 0 0 4l5 4V5.5c4 0 7 1.5 8 6.5 0-6-3-9-8-9z" fill="#111"/></svg>Unfollow</div>
    </div></div>
  <div class="col"><div class="card"><div class="thumb" role="img" aria-label="Silver smartphone" style="width:70px;background:linear-gradient(#d8d8d8,#8d8d8d)"></div></div>
    <div class="actions">
      <div class="act"><svg width="17" height="12" viewBox="0 0 17 12"><path d="M0 1h6l2 2h9v9H0z" fill="#111"/></svg>Share</div>
      <div class="act"><svg width="16" height="13" viewBox="0 0 16 13"><path d="M0 1h3l2 8h9l2-6H4" stroke="#111" stroke-width="1.4" fill="none"/><circle cx="6" cy="11.5" r="1.3"/><circle cx="13" cy="11.5" r="1.3"/></svg>Buy</div>
      <div class="act"><svg width="14" height="13" viewBox="0 0 14 13"><path d="M5 0 0 4l5 4V5.5c4 0 7 1.5 8 6.5 0-6-3-9-8-9z" fill="#111"/></svg>Unfollow</div>
    </div></div>
  <div class="col"><div class="card"><div class="thumb" role="img" aria-label="Tablet with colourful tiled screen" style="background:linear-gradient(135deg,#2d2d3a,#6a3fa0)"></div></div>
    <div class="actions">
      <div class="act"><svg width="17" height="12" viewBox="0 0 17 12"><path d="M0 1h6l2 2h9v9H0z" fill="#111"/></svg>Share</div>
      <div class="act"><svg width="16" height="13" viewBox="0 0 16 13"><path d="M0 1h3l2 8h9l2-6H4" stroke="#111" stroke-width="1.4" fill="none"/><circle cx="6" cy="11.5" r="1.3"/><circle cx="13" cy="11.5" r="1.3"/></svg>Buy</div>
      <div class="act"><svg width="14" height="13" viewBox="0 0 14 13"><path d="M5 0 0 4l5 4V5.5c4 0 7 1.5 8 6.5 0-6-3-9-8-9z" fill="#111"/></svg>Unfollow</div>
    </div></div>
</div>

<h2 class="abs section-title" style="top:651px;font-weight:400">Products That Other People Follow</h2>
<div class="abs pager" style="top:652px">
  <span><svg width="8" height="8" viewBox="0 0 8 8"><path d="M5 1 2 4l3 3" stroke="#fff" stroke-width="1.6" fill="none"/></svg></span>
  <span><svg width="8" height="8" viewBox="0 0 8 8"><path d="M3 1l3 3-3 3" stroke="#fff" stroke-width="1.6" fill="none"/></svg></span>
</div>
<div class="abs section-rule" style="top:677px"></div>

<div class="abs row" style="top:697px">
  <div class="col"><div class="card"><div class="thumb" role="img" aria-label="Laptop showing a beach scene" style="background:linear-gradient(#6fb3c9,#c9b98a)"></div></div>
    <div class="follow-btn"><svg width="13" height="12" viewBox="0 0 13 12"><path d="M8 0l5 4-5 4V5.5C4 5.5 1.5 7 0 12 0 6 3 3 8 3z" fill="#111"/></svg>Follow</div></div>
  <div class="col"><div class="card"><div class="thumb" role="img" aria-label="Row of colourful music players" style="background:linear-gradient(90deg,#333,#e07aa0,#d8c64a,#5ab0d8)"></div></div>
    <div class="follow-btn"><svg width="13" height="12" viewBox="0 0 13 12"><path d="M8 0l5 4-5 4V5.5C4 5.5 1.5 7 0 12 0 6 3 3 8 3z" fill="#111"/></svg>Follow</div></div>
  <div class="col"><div class="card"><div class="thumb" role="img" aria-label="Boxed pink towel set" style="background:linear-gradient(90deg,#c0204a,#7a2a6a,#333)"></div></div>
    <div class="follow-btn"><svg width="13" height="12" viewBox="0 0 13 12"><path d="M8 0l5 4-5 4V5.5C4 5.5 1.5 7 0 12 0 6 3 3 8 3z" fill="#111"/></svg>Follow</div></div>
  <div class="col"><div class="card"><div class="thumb" role="img" aria-label="Black smartphone front and side" style="width:55px;background:linear-gradient(#3a3a3a,#111)"></div></div>
    <div class="follow-btn"><svg width="13" height="12" viewBox="0 0 13 12"><path d="M8 0l5 4-5 4V5.5C4 5.5 1.5 7 0 12 0 6 3 3 8 3z" fill="#111"/></svg>Follow</div></div>
</div>

<div class="abs friend-col" style="left:90px">
  <div class="friend"><div class="avatar"><div role="img" aria-label="Friend profile photo" style="background:linear-gradient(#7a5a4a,#2a2020)"></div></div><div><div class="friend-name">Mara</div><div class="following">Following</div></div></div>
  <div class="friend"><div class="avatar"><div role="img" aria-label="Friend profile photo" style="background:linear-gradient(#c9b8a8,#2a2e3a)"></div></div><div><div class="friend-name">Mara</div><div class="following">Following</div></div></div>
</div>
<div class="abs friend-col" style="left:256px">
  <div class="friend"><div class="avatar"><div role="img" aria-label="Friend profile photo" style="background:linear-gradient(#eee,#3a2a2a)"></div></div><div><div class="friend-name">Mara</div><div class="following">Following</div></div></div>
  <div class="friend"><div class="avatar"><div role="img" aria-label="Friend profile photo" style="background:linear-gradient(#eee,#222)"></div></div><div><div class="friend-name">Mara</div><div class="following">Following</div></div></div>
</div>
<div class="abs friend-col" style="left:421px">
  <div class="friend"><div class="avatar"><div role="img" aria-label="Friend profile photo" style="background:linear-gradient(#c8b0a0,#1f1f2a)"></div></div><div><div class="friend-name">Mara</div><div class="following">Following</div></div></div>
  <div class="friend"><div class="avatar"><div role="img" aria-label="Friend profile photo" style="background:linear-gradient(#5a3a2a,#1a1210)"></div></div><div><div class="friend-name">Mara</div><div class="following">Following</div></div></div>
</div>
<div class="abs friend-col" style="left:587px;border-right:0">
  <div class="friend"><div class="avatar"><div role="img" aria-label="Friend profile photo" style="background:linear-gradient(#ddd,#6a4a30)"></div></div><div><div class="friend-name">Mara</div><div class="following">Following</div></div></div>
  <div class="friend"><div class="avatar"><div role="img" aria-label="Friend profile photo" style="background:linear-gradient(#e8c890,#6a9a50)"></div></div><div><div class="friend-name">Mara</div><div class="following">Following</div></div></div>
</div>

<p class="abs friend-note" style="left:90px">Friend1, Friend2 and 5 others are following this product</p>
<p class="abs friend-note" style="left:262px">Friend1, Friend2 and 5 others are following this product</p>
<p class="abs friend-note" style="left:428px">Friend1, Friend2 and 5 others are following this product</p>
<p class="abs friend-note" style="left:596px">Friend1, Friend2 and 5 others are following this product</p>

<footer class="abs footer">
  <div class="foot-links"><span>Home</span>|<span>About Us</span>|<span>Products URl</span>|<span>Testimonials</span>|<span>FAQ's</span>|<span>Contact Us</span></div>
  <div class="foot-links foot-copy"><span>©2013 Company Name , All Rights Reserved</span>|<span>Privacy Policy</span>|<span>Terms &amp; Conditions</span></div>
  <div class="social" aria-label="Social links"><i></i><i></i><i></i><i></i></div>
</footer>
</body>
</html>
```